Business Card Design for a Sound engineer and DJ

We would like a residn of the business card.

Logo must remain the same.
The card is for the owner of the company.
The business card is in Arabic as the company is based in Kuwait.
The company specializes in sound engineering for singers concerts and events and in addition DJ.
The color options is up to the designer but we would like it masculine as the owner is a man.

Target Market(s)

All ages

Industry/Entity Type

Media

Contact Information for Business Card

Name:
Eng. Faisal Barrak
م/فيصل براك

The name above is in Arabic and English.

Title: General Manager
Mobile: +965 96370482
Office: +965 22480637
Email: info@qamarwave.net

Address:
Office no. 3
1st floor
Marjan Complex
Hamad Faraj St.
Salmiya
Kuwait

Instagram: @qamarwave
Snap: qamarwave

Requirements
Nice to have
• can we have Instagram icon and snap icon and a phone vector and email?
• Instead of writing the words

```html
<!DOCTYPE html>
<html lang="en">
<head>
<meta charset="utf-8">
<title>Qamar Wave Business Card</title>
<link rel="stylesheet" href="https://fonts.googleapis.com/css2?family=Roboto:wght@400;500&family=Cairo:wght@400;600&display=swap">
<style>
  :root {
    --backdrop: #2b2b2d;
    --ink-black: #050505;
    --paper: #ffffff;
    --magenta: #e0217f;
    --violet: #8a5fc4;
    --lilac: #b58ee0;
    --text-grey: #6a6a6a;
    --band: linear-gradient(90deg, #e8238a 0%, #c04aa8 55%, #8f6ad0 100%);
  }
  * { margin: 0; padding: 0; box-sizing: border-box; }
  html, body { width: 1200px; height: 900px; overflow: hidden; }
  body {
    background: var(--backdrop);
    font-family: "Roboto", Arial, sans-serif;
    position: relative;
  }
  .card {
    position: absolute;
    top: 130px;
    width: 366px;
    height: 640px;
    border-radius: 26px;
    overflow: hidden;
    background: var(--ink-black);
  }
  .card--front { left: 200px; }
  .card--back { left: 634px; }

  .brand {
    position: absolute;
    left: 0; right: 0;
    text-align: center;
  }
  .card--front .brand { top: 110px; }
  .card--back .brand { top: 220px; }
  .brand__mark {
    display: inline-flex;
    align-items: center;
    gap: 10px;
    font-family: "Roboto", Arial, sans-serif;
    font-weight: 500;
    font-size: 34px;
    letter-spacing: 3px;
    color: var(--lilac);
    text-transform: uppercase;
  }
  .brand__dot {
    width: 14px; height: 14px;
    border-radius: 50%;
    background: var(--magenta);
  }
  .brand__tagline {
    margin-top: 8px;
    font-size: 12px;
    letter-spacing: 1.5px;
    color: var(--violet);
  }
  .brand__tagline-ar {
    margin-top: 2px;
    font-family: "Cairo", Arial, sans-serif;
    font-size: 14px;
    color: var(--violet);
    direction: rtl;
  }

  .front__info {
    position: absolute;
    left: 0; top: 290px;
    width: 366px; height: 312px;
    background: var(--paper);
    border-bottom-right-radius: 22px;
    padding: 22px 26px 0 40px;
  }
  .front__marker {
    position: absolute;
    left: 0; top: 30px;
  }
  .person__name-row {
    display: flex;
    justify-content: space-between;
    align-items: baseline;
  }
  .person__name {
    font-size: 19px;
    color: var(--magenta);
  }
  .person__name-ar {
    font-family: "Cairo", Arial, sans-serif;
    font-weight: 600;
    font-size: 17px;
    color: var(--violet);
    direction: rtl;
  }
  .person__title {
    font-size: 13px;
    color: var(--text-grey);
    margin-top: 2px;
    margin-bottom: 18px;
  }
  .contact { list-style: none; }
  .contact__row {
    display: flex;
    align-items: center;
    gap: 10px;
    height: 26px;
    font-size: 13.5px;
    color: var(--text-grey);
  }
  .contact__pair { display: flex; gap: 26px; }
  .contact__pair span { display: flex; align-items: center; gap: 10px; }
  .contact__icon { width: 20px; height: 20px; flex: none; }
  .contact__address {
    margin-top: 12px;
    font-size: 13.5px;
    line-height: 1.45;
    color: var(--text-grey);
  }

  .front__band {
    position: absolute;
    left: 0; bottom: 0;
    width: 100%; height: 48px;
    background: var(--band);
  }
  .back__band {
    position: absolute;
    left: 0; bottom: 22px;
    width: 100%; height: 18px;
    background: var(--band);
  }
</style>
</head>
<body>

<section class="card card--front" aria-label="Card front">
  <div class="brand">
    <div class="brand__mark"><span class="brand__dot"></span>Qamar Wave</div>
    <div class="brand__tagline">DJ - SOUND ENG. - LIGHTING</div>
    <div class="brand__tagline-ar">دي جي · هندسة صوت · إضاءة</div>
  </div>

  <div class="front__band"></div>

  <div class="front__info">
    <svg class="front__marker" width="16" height="26" viewBox="0 0 16 26"><polygon points="0,0 16,13 0,26" fill="#8a5fc4"/></svg>
    <div class="person__name-row">
      <span class="person__name">Eng. Faisal Barrak</span>
      <span class="person__name-ar">م/فيصل براك</span>
    </div>
    <div class="person__title">General Manager</div>

    <ul class="contact">
      <li class="contact__row">
        <svg class="contact__icon" viewBox="0 0 20 20"><circle cx="10" cy="10" r="9" fill="none" stroke="#e0217f" stroke-width="1.5"/><path d="M7 6c-1 1 0 4 2 6s5 3 6 2l-1.5-1.5-1.5 1c-1-.5-2.5-2-3-3l1-1.5z" fill="#e0217f"/></svg>
        +965 22480637
      </li>
      <li class="contact__row">
        <svg class="contact__icon" viewBox="0 0 20 20"><circle cx="10" cy="10" r="9" fill="none" stroke="#e0217f" stroke-width="1.5"/><rect x="7" y="5" width="6" height="10" rx="1" fill="none" stroke="#e0217f" stroke-width="1.4"/><circle cx="10" cy="13" r=".8" fill="#e0217f"/></svg>
        +965 96370482
      </li>
      <li class="contact__row">
        <svg class="contact__icon" viewBox="0 0 20 20"><circle cx="10" cy="10" r="9" fill="none" stroke="#e0217f" stroke-width="1.5"/><rect x="5.5" y="6.5" width="9" height="7" fill="none" stroke="#e0217f" stroke-width="1.3"/><path d="M5.5 6.5l4.5 4 4.5-4" fill="none" stroke="#e0217f" stroke-width="1.3"/></svg>
        info@qamarwave.net
      </li>
      <li class="contact__row contact__pair">
        <span><svg class="contact__icon" viewBox="0 0 20 20"><circle cx="10" cy="10" r="9" fill="none" stroke="#e0217f" stroke-width="1.5"/></svg>@qamarwave</span>
        <span><svg class="contact__icon" viewBox="0 0 20 20"><circle cx="10" cy="10" r="9" fill="none" stroke="#e0217f" stroke-width="1.5"/></svg>qamarwave</span>
      </li>
    </ul>

    <p class="contact__address">Office no. 3, 1st floor, Marjan Complex,<br>Hamad Faraj St., Salmiya, Kuwait</p>
  </div>
</section>

<section class="card card--back" aria-label="Card back">
  <div class="brand">
    <div class="brand__mark"><span class="brand__dot"></span>Qamar Wave</div>
    <div class="brand__tagline">DJ - SOUND ENG. - LIGHTING</div>
    <div class="brand__tagline-ar">دي جي · هندسة صوت · إضاءة</div>
  </div>
  <div class="back__band"></div>
</section>

</body>
</html>
```